KV Group

We need a new website for our company and since we had a very good work done for our logo in this site, we're back for the entire job.

Our company name is Marlowe Capital Group. We're adding files of examples of what we have done today. In my opinion we need a more attention lock in the site but yet financial simple work.

Our files (attached) will let you know what we have so far. We need a complete change but the colours should be the same, however you can change them not running away to far from the original, and of course matching with the logo.

We need examples for 3 kind of layouts.

- A HOME welcome layout
- An internal Layout with sidebar
- And internal Layout wide

We can buy image licenses if needed for assets.
Actually there are 5 slide images placed on the Welcome HOME, we need those there, but you can improve with better images to match the new website!!!

Target Market(s)

Clients looking for financial advisers, tax and funds specialist, currency advisers

Industry/Entity Type

Financial

Requirements
Must have
• all the fonts must be in accordance with the financial market sites........the welcome home page must be precise, neat and information accurate........the menu should be elegant........main focus on the Home page, should be also the PRIVATE ACCESS box log in.......

```html
<!DOCTYPE html>
<html lang="en">
<head>
<meta charset="utf-8">
<title>Marlowe Capital Group</title>
<link href="https://fonts.googleapis.com/css2?family=Questrial&family=Open+Sans:wght@400;600;700&family=Fjalla+One&display=swap" rel="stylesheet">
<style>
:root{
  --orange:#f07a1e;
  --brown-dark:#5c4636;
  --brown-band:#bf9e85;
  --brown-strip:#a47f66;
  --frame:#cdbcad;
  --text:#555;
  --muted:#888;
  --line:#ddd;
  --blue:#2a63a8;
  --green:#3a8f2e;
  --red:#d0202a;
  --badge-blue:#2e5aa6;
  --badge-green:#7ab648;
  --badge-navy:#1f3f8c;
  --badge-red:#a4233a;
}
*{margin:0;padding:0;box-sizing:border-box}
html,body{width:792px;height:1200px;overflow:hidden;background:#fff}
body{position:relative;font-family:"Open Sans",Arial,sans-serif;color:var(--text)}
.abs{position:absolute}
.site-header{left:0;top:0;width:792px;height:92px;background:linear-gradient(#fff,#ececec)}
.brand{left:108px;top:12px;display:flex;align-items:center;gap:8px;font-weight:700;font-size:11px;letter-spacing:.5px;color:#444}
.brand-mark{width:26px;height:26px;background:var(--orange)}
.top-actions{left:405px;top:0;width:295px;height:66px;background:linear-gradient(#fafafa,#efefef);border-radius:0 0 30px 30px;box-shadow:0 2px 4px rgba(0,0,0,.08)}
.top-link{top:24px;font-size:12px;color:#222;display:flex;align-items:center;gap:8px}
.main-nav{left:93px;top:75px;width:607px;height:26px;border-radius:13px;background:linear-gradient(#fff,#e8e8e8);box-shadow:0 1px 3px rgba(0,0,0,.2);display:flex;align-items:center;padding-left:11px}
.main-nav a{font-size:8.5px;color:#444;text-decoration:none;padding:0 9px;height:26px;line-height:26px;border-right:1px solid #d6d6d6}
.main-nav a.active{background:var(--orange);color:#fff;padding:0 12px;height:24px;line-height:24px}
.hero{left:93px;top:111px;width:447px;height:206px;border-radius:3px;overflow:hidden;background:linear-gradient(135deg,#e9dccb 0%,#b89a78 45%,#6e5640 100%)}
.hero-caption{left:0;bottom:0;width:100%;height:70px;background:rgba(40,30,20,.7);padding:8px 23px;color:#fff}
.hero-caption h2{font-weight:400;font-size:19px;line-height:20px}
.hero-caption p{font-size:9px;line-height:13px;margin-top:2px}
.private{left:547px;top:111px;width:152px;height:206px;background:var(--brown-dark);border-radius:3px}
.private h3{color:#fff;font-size:13px;font-weight:700;margin:7px 0 0 7px}
.private-panel{left:6px;top:31px;width:140px;height:168px;border-radius:3px;background:linear-gradient(#f3e6d6,#dcc0a3)}
.private label{display:block;font-size:8px;line-height:11px;color:#333;margin:7px 0 0 6px}
.private label:first-child{margin-top:9px}
.field{margin:5px 0 0 6px;width:128px;height:20px;border-radius:3px;background:#5b4a3d}
.forgot{font-size:8px;line-height:11px;color:#333;margin:7px 0 0 6px}
.login-btn{margin:11px 0 0 7px;width:81px;height:19px;border-radius:3px;background:linear-gradient(#ffc42e,#f3960e);border:1px solid #c5780c;font-size:8px;font-weight:700;color:#3a2a10;text-align:center;line-height:17px}
.welcome{left:93px;top:338px;width:606px;height:92px;border:1px solid #e6e6e6;background:linear-gradient(#fff,#f6f6f6);padding:12px 14px}
.welcome h1{font-family:"Questrial",sans-serif;font-weight:400;font-size:20px;color:#222}
.welcome p{font-size:7.6px;line-height:14px;color:#444;margin-top:6px}
.services{left:93px;top:456px;width:606px;height:281px;background:var(--frame);border-radius:4px;border:1px solid #b9a693}
.service{top:9px;width:188px;height:262px;background:#fff;padding:3px}
.service-img{width:182px;height:125px}
.service h4{font-family:"Fjalla One",sans-serif;font-weight:400;font-size:15px;color:#3a3a3a;margin:11px 0 0 10px;letter-spacing:.4px}
.service p{font-size:7.6px;line-height:14.2px;color:#555;margin:7px 8px 0 10px}
.services-shadow{left:130px;top:738px;width:530px;height:10px;border-radius:50%;background:radial-gradient(rgba(0,0,0,.25),transparent 70%)}
.ticker{left:100px;top:762px;width:592px;height:20px;border:2px solid #f3e6dc;display:flex;align-items:center;gap:14px;padding-left:8px;font-size:6.8px;font-weight:700;white-space:nowrap;overflow:hidden}
.ticker .pair{color:var(--blue)}
.up{color:var(--green)}
.down{color:var(--red)}
.verified-title{left:0;top:795px;width:792px;text-align:center;font-size:12px;font-weight:700;color:#222}
.verified-label{left:117px;top:836px;font-size:9.5px;font-weight:600;color:#222}
.badge{position:absolute}
.divider{left:100px;top:881px;width:592px;height:1px;background:var(--line)}
.footer-col h5{font-family:"Questrial",sans-serif;font-weight:400;font-size:12px;color:#333;margin-bottom:6px}
.footer-col li{list-style:none;font-size:8px;line-height:14.2px;color:var(--muted)}
.about-band{left:0;top:1052px;width:792px;height:123px;background:var(--brown-band);padding:11px 111px 0;color:#fff}
.about-band p{font-size:7.6px;line-height:14px;margin-bottom:15px}
.copyright{left:0;top:1175px;width:792px;height:25px;background:var(--brown-strip);color:#fff;font-size:8px;text-align:center;line-height:25px}
</style>
</head>
<body>
<header class="site-header abs">
  <div class="brand abs"><span class="brand-mark"></span>MARLOWE CAPITAL GROUP</div>
  <div class="top-actions abs"></div>
  <a class="top-link abs" style="left:452px">
    <svg width="14" height="14" viewBox="0 0 14 14"><rect x="1" y="1" width="12" height="12" fill="none" stroke="#f07a1e" stroke-width="1.6"/><path d="M4 10 L10 4" stroke="#f07a1e" stroke-width="1.6"/></svg>Apply Now</a>
  <a class="top-link abs" style="left:583px">
    <svg width="14" height="12" viewBox="0 0 14 12"><rect x="0" y="1" width="14" height="10" fill="#f07a1e"/><path d="M0 1 L7 7 L14 1" fill="none" stroke="#fff" stroke-width="1.2"/></svg>Contact Us</a>
</header>

<nav class="main-nav abs">
  <a class="active">HOME</a><a>ABOUT US</a><a>INVESTMENTS</a><a>FUNDS</a><a>BROKERAGE</a><a>EXCHANGE</a><a style="border:none">ACCOUNTS</a>
</nav>

<section class="hero abs" role="img" aria-label="Sepia photo of currency symbols over a calendar grid">
  <div class="hero-caption abs">
    <h2>Online services</h2>
    <p>Manage your everyday finances easily with eBanking. <span style="font-size:12px">Online services</span> are available, whenever it is most convenient.</p>
  </div>
</section>

<aside class="private abs">
  <h3>Private Access</h3>
  <div class="private-panel abs">
    <label>Acc. Number</label><div class="field"></div>
    <label>Acc. Password</label><div class="field"></div>
    <p class="forgot">Forgot acc number/password?</p>
    <div class="login-btn">Log in to Accounts</div>
  </div>
</aside>

<section class="welcome abs">
  <h1>Welcome to Marlowe Capital Group</h1>
  <p>Lorem ipsum dolor sit amet, consectetur adipisicing elit, sed do eiusmod tempor incididunt ut labore et dolore magna aliqua. Ut enim ad minim veniam, quis nostrud exercitation ullamco laboris nisi ut aliquip ex ea commodo consequat. Duis aute irure dolor in reprehenderit in voluptate velit esse cillum dolore eu fugiat nulla pariatur. Excepteur sint occaecat cupidatat non proident, sunt in culpa qui officia deserunt mollit anim id est laborum.</p>
</section>

<section class="services abs">
  <article class="service abs" style="left:8px">
    <div class="service-img" role="img" aria-label="Photo of a hand with a pen over financial bar charts" style="background:linear-gradient(135deg,#f4f4f2,#cfd8c4 60%,#9cc24a)"></div>
    <h4>MANAGEMENT &amp; STRATEGY</h4>
    <p>Lorem ipsum dolor sit amet, consectetur adipisicing elit, sed do eiusmod tempor incididunt ut labore et dolore magna aliqua. Ut enim ad minim veniam, quis nostrud exercitation ullamco laboris nisi ut aliquip ex ea commodo consequat.</p>
  </article>
  <article class="service abs" style="left:207px">
    <div class="service-img" role="img" aria-label="Photo of two business people shaking hands" style="background:linear-gradient(135deg,#dfe9f1,#b9cbd9 55%,#7d8b98)"></div>
    <h4>FUNDS</h4>
    <p>Lorem ipsum dolor sit amet, consectetur adipisicing elit, sed do eiusmod tempor incididunt ut labore et dolore magna aliqua. Ut enim ad minim veniam, quis nostrud exercitation ullamco laboris nisi ut aliquip ex ea commodo consequat.</p>
  </article>
  <article class="service abs" style="left:406px">
    <div class="service-img" role="img" aria-label="Illustration of currency symbols standing on a globe" style="background:linear-gradient(#2c4a78,#1a2f55 60%,#3b6aa8)"></div>
    <h4>CURRENCY EXCHANGE</h4>
    <p>Lorem ipsum dolor sit amet, consectetur adipisicing elit, sed do eiusmod tempor incididunt ut labore et dolore magna aliqua. Ut enim ad minim veniam, quis nostrud exercitation ullamco laboris nisi ut aliquip ex ea commodo consequat.</p>
  </article>
</section>
<div class="services-shadow abs"></div>

<div class="ticker abs">
  <span><span class="pair">GBP/FJD =</span> <span class="down">2.96102 ▼</span></span>
  <span><span class="pair">GBP/GMD =</span> <span class="up">51.07976 ▲</span></span>
  <span><span class="pair">GBP/GNF =</span> <span class="down">10769.81405 ▼</span></span>
  <span><span class="pair">GBP/GTQ =</span> <span class="up">12.50894 ▲</span></span>
  <span><span class="pair">GBP/HKD =</span> <span class="up">12.18193 ▲</span></span>
  <span><span class="pair">GBP/HNL =</span> <span class="up">31.99</span></span>
</div>

<h2 class="verified-title abs">Verified and Protected by</h2>
<p class="verified-label abs">Verified and Protected by</p>
<svg class="badge" style="left:270px;top:826px" width="88" height="36" role="img" aria-label="Partner badge"><rect width="88" height="36" fill="var(--badge-blue)"/></svg>
<svg class="badge" style="left:390px;top:828px" width="104" height="30" role="img" aria-label="Certification badge"><rect width="104" height="30" rx="3" fill="var(--badge-green)"/></svg>
<svg class="badge" style="left:515px;top:822px" width="44" height="44" role="img" aria-label="Certification badge"><circle cx="22" cy="22" r="21" fill="var(--badge-navy)"/></svg>
<svg class="badge" style="left:588px;top:824px" width="88" height="36" role="img" aria-label="Security badge"><rect width="88" height="36" rx="18" fill="var(--badge-red)"/></svg>

<div class="divider abs"></div>

<div class="footer-col abs" style="left:111px;top:892px"><h5>ABOUT US</h5><ul><li>History</li><li>Expertize</li><li>Identity</li><li>Strategy</li><li>Contact Us</li></ul></div>
<div class="footer-col abs" style="left:198px;top:892px"><h5>INVESTMENTS</h5><ul><li>Term Deposits</li><li>Managment &amp; Strategy</li><li>Client Relations</li><li>Financial Privacy</li><li>Tax Advice</li><li>Wealth Analysis &amp; Financial Planning</li><li>Active Advisory Group</li><li>Manager Selection Services</li><li>Private Equity</li></ul></div>
<div class="footer-col abs" style="left:366px;top:892px"><h5>FUNDS</h5><ul><li>Overview</li><li>Administration</li><li>Funds Security</li><li>Core Services</li><li>Reporting</li><li>Revenue Opotunities</li><li>How it works?</li><li>Glossary</li></ul></div>
<div class="footer-col abs" style="left:477px;top:890px"><h5>CURRENCY EXCHANGE</h5><ul><li>Foreign Exchange</li><li>Fx Forward</li><li>Fx Options</li></ul></div>
<div class="footer-col abs" style="left:477px;top:968px"><h5>ACCOUNTS</h5><ul><li>Apply Now</li><li>Private Access</li></ul></div>
<div class="footer-col abs" style="left:620px;top:890px"><h5>BROKERAGE</h5><ul><li>Institutional</li><li>Research</li><li>Trading</li></ul></div>

<section class="about-band abs">
  <p>Lorem ipsum dolor sit amet, consectetur adipisicing elit, sed do eiusmod tempor incididunt ut labore et dolore magna aliqua. Ut enim ad minim veniam, quis nostrud exercitation ullamco laboris nisi ut aliquip ex ea commodo consequat. Duis aute irure dolor in reprehenderit in voluptate velit esse cillum dolore eu fugiat nulla pariatur. Excepteur sint occaecat cupidatat non proident, sunt in culpa qui officia deserunt mollit anim id est laborum.</p>
  <p>Lorem ipsum dolor sit amet, consectetur adipisicing elit, sed do eiusmod tempor incididunt ut labore et dolore magna aliqua. Ut enim ad minim veniam, quis nostrud exercitation ullamco laboris nisi ut aliquip ex ea commodo consequat. Duis aute irure dolor in reprehenderit in voluptate velit esse cillum dolore eu fugiat nulla pariatur. Excepteur sint occaecat cupidatat non proident, sunt in culpa qui officia deserunt mollit anim id est laborum.</p>
</section>
<footer class="copyright abs">© 2013 Marlowe Capital Group &nbsp;|&nbsp; Legal Disclaimer</footer>
</body>
</html>
```